Power point presentation optimization, in terms of content design

I have a completed business presentation, with all the texting, but I need some design improvement in terms of text formatting, lettering, text boxes, arrows, bullets, shapes and their formatting, relative location of text boxes and pictures in the slide, etc, etc, so that this specific presentation becomes more visually appealing.
Our company power point template is available.
I´m providing our company power point template (to be used as a reference) as well as the presentation that needs to be improved.

Target Market(s)

Potential partner in business.

Industry/Entity Type

Health

Requirements
Nice to have
• More ellegant collors (more according to the template) on the picture of slide 7. A more elegant dollar image (slide 16).

```html
<!DOCTYPE html>
<html lang="pt">
<head>
<meta charset="utf-8">
<title>Centro Vértice de Telemedicina — Apresentação</title>
<link href="https://fonts.googleapis.com/css2?family=Open+Sans:wght@300;400;600;700&family=Poppins:wght@400;500;600;700&display=swap" rel="stylesheet">
<style>
:root{
  --canvas:#cfcfcf;
  --navy:#21508a;
  --blue:#2e6aa3;
  --teal:#3f8fb8;
  --sky:#5aa3c8;
  --ink:#222;
  --grey-band:#ececec;
  --white:#fff;
}
*{margin:0;padding:0;box-sizing:border-box}
html,body{width:1200px;height:1174px;overflow:hidden;background:var(--canvas)}
body{position:relative;font-family:"Poppins",sans-serif;color:var(--ink)}
.slide{position:absolute;width:320px;height:239px;background:var(--white);overflow:hidden;box-shadow:2px 3px 6px rgba(0,0,0,.25)}
.abs{position:absolute}
.slide-head{position:absolute;left:0;top:0;width:100%;height:26px;
  background:linear-gradient(112deg,#3a6c9f 0 68%,#2b5a8e 68% 75%,#4c80b3 75% 80%,#234e82 80% 88%,#3b73a8 88% 93%,#21497c 93%);
  border-bottom:1.5px solid #fff;box-shadow:0 1.5px 0 #c8ccd2}
.slide-title{position:absolute;left:9px;top:10px;font-family:"Open Sans",sans-serif;font-weight:400;font-size:10.5px;color:#fff;letter-spacing:.2px}
.slide-foot{position:absolute;left:0;bottom:0;width:100%;height:15px;background:var(--navy)}
.foot-accent{position:absolute;left:0;top:0;width:34px;height:15px;background:var(--teal);clip-path:polygon(0 0,100% 0,62% 100%,0 100%)}
.foot-logo{position:absolute;left:18px;top:0;width:60px;height:15px;background:#fff;clip-path:polygon(22% 0,100% 0,86% 100%,0 100%)}
.foot-logo span{position:absolute;left:12px;top:4px;font-size:5.5px;font-weight:700;color:var(--blue);letter-spacing:.3px}
.foot-logo i{position:absolute;left:6px;top:4.5px;width:5px;height:5px;background:var(--blue)}
.foot-url{position:absolute;right:5px;top:4.5px;font-size:3.8px;color:#fff;font-weight:500}
.sub-title{position:absolute;font-weight:600;font-size:8px;color:var(--teal);letter-spacing:.2px}
.tiny{font-size:5px;line-height:1.25}
.center{text-align:center}
.photo{position:absolute}
.cover-logo{position:absolute;left:0;top:183px;width:100%;height:37px;background:#fff;border-bottom:1px solid #bfc6cf}
.cover-logo .mark{position:absolute;left:20px;top:9px;width:18px;height:18px;background:var(--blue)}
.cover-logo .name{position:absolute;left:44px;top:7px;font-weight:700;font-size:11px;color:var(--blue);letter-spacing:.3px}
.cover-logo .person{position:absolute;left:44px;top:23px;font-size:5.6px;color:#444}
.cover-band{position:absolute;left:0;bottom:0;width:100%;height:19px;background:linear-gradient(90deg,#2f66a0,#3e7cb2)}
.cover-title{position:absolute;left:22px;top:115px;color:#fff;font-family:"Open Sans",sans-serif;font-size:14.5px;line-height:1.5}
.cover-title b{font-weight:700}
.context-caption{position:absolute;top:110px;font-size:6px;line-height:1.3}
</style>
</head>
<body>

<section class="slide" style="left:219px;top:54px">
  <div class="abs" style="left:0;top:0;width:320px;height:183px;background:#000"></div>
  <svg class="abs" style="left:0;top:0" width="320" height="183"><polygon points="292,0 320,0 320,40" fill="#fff"/></svg>
  <div class="cover-logo"><i class="mark"></i><div class="name">CENTRO VÉRTICE</div><div class="person">Professor Doutor Rui Tavares</div></div>
  <div class="cover-band"></div>
</section>

<section class="slide" style="left:659px;top:54px;width:321px">
  <div class="photo" role="img" aria-label="Retrato de médico sorridente sob véu azul" style="left:0;top:0;width:321px;height:239px;background:linear-gradient(135deg,#5b8fbd,#3f74a8 55%,#7aa6cc)"></div>
  <svg class="abs" style="left:0;top:0" width="321" height="183"><polygon points="238,0 321,0 321,85" fill="#fff"/></svg>
  <svg class="abs" style="left:22px;top:70px" width="36" height="34" fill="none" stroke="#fff" stroke-width="1.4"><rect x="2" y="2" width="18" height="29" rx="2"/><path d="M7 8v6a4 4 0 0 0 8 0V8M11 18v5h9"/><circle cx="29" cy="10" r="2.5"/><path d="M25 4a7 7 0 0 1 8 0"/></svg>
  <div class="cover-title">Centro Vértice de Telemedicina<br><b>Uma perspetiva de 5 minutos</b></div>
  <div class="cover-logo" style="background:rgba(255,255,255,.94)"><i class="mark"></i><div class="name">CENTRO VÉRTICE</div><div class="person">Professor Doutor Rui Tavares</div></div>
  <div class="cover-band" style="opacity:.85"></div>
</section>

<section class="slide" style="left:92px;top:340px">
  <header class="slide-head"><h2 class="slide-title">IMAGIOLOGIA EM ANGOLA</h2></header>
  <div class="sub-title" style="left:20px;top:60px">CONTEXTO DE OPORTUNIDADE</div>
  <div class="abs" style="left:0;top:107px;width:200px;height:32px;background:var(--grey-band)"></div>
  <svg class="abs" style="left:0;top:0" width="320" height="239"><polygon points="215,95 320,95 320,165 160,165" fill="var(--teal)"/>
    <circle cx="28" cy="94" r="11" fill="var(--teal)"/><path d="M23 88l10 12M33 88l-10 12" stroke="#fff" stroke-width="1.3"/>
    <circle cx="107" cy="94" r="11" fill="var(--teal)"/><g fill="#fff"><circle cx="103" cy="91" r="2"/><circle cx="111" cy="91" r="2"/><circle cx="107" cy="89" r="2.3"/><ellipse cx="107" cy="98" rx="6" ry="3"/></g>
    <line x1="92" y1="112" x2="92" y2="121" stroke="#555" stroke-width=".6"/>
    <path d="M188 114h7" stroke="var(--teal)" stroke-width="1"/><polygon points="195,112 199,114 195,116" fill="var(--teal)"/>
    <g stroke="#fff" stroke-width="1.2" fill="none"><path d="M216 136h20M218 135v-6M223 135v-9M228 135v-7M233 135v-12M216 126l8-6 5 3 8-8"/></g>
  </svg>
  <p class="context-caption" style="left:17px;width:70px">Carência dramática de cuidados na área da Imagiologia</p>
  <p class="context-caption" style="left:100px;width:80px">População urbana em rápido crescimento. Aumento do PIB</p>
  <p class="abs" style="left:215px;top:140px;width:95px;font-size:6px;font-weight:600;color:#fff;line-height:1.3">Oportunidade comercial relevante</p>
  <footer class="slide-foot"><i class="foot-accent"></i><div class="foot-logo"><i></i><span>VÉRTICE</span></div><span class="foot-url">www.verticetelemed.com | 2</span></footer>
</section>

<section class="slide" style="left:446px;top:340px">
  <header class="slide-head"><h2 class="slide-title">IMAGIOLOGIA EM ANGOLA</h2></header>
  <svg class="abs" style="left:0;top:0" width="320" height="239" role="img" aria-label="Médica a analisar imagens em vários monitores">
    <defs><linearGradient id="g1" x1="0" x2="1"><stop offset="0" stop-color="#1d3f63"/><stop offset=".6" stop-color="#3d6f9a"/><stop offset="1" stop-color="#9ab7cf"/></linearGradient></defs>
    <polygon points="140,27 320,27 320,160 232,156" fill="url(#g1)"/>
    <polygon points="0,169 320,153 320,213 0,213" fill="var(--teal)"/>
  </svg>
  <div class="sub-title center" style="left:83px;top:59px;width:60px;font-size:6.2px">A DIFICULDADE</div>
  <svg class="abs" style="left:0;top:0" width="320" height="239" fill="none" stroke="var(--blue)" stroke-width=".9">
    <rect x="71" y="76" width="11" height="11"/><path d="M76.5 77v9M73 80h7M73 83h7"/>
    <path d="M147 76l8 11M155 76l-8 11" stroke-width="1.1"/>
    <circle cx="48" cy="128" r="2.6" fill="var(--blue)"/><path d="M42 135a6 4 0 0 1 12 0z" fill="var(--blue)"/>
    <path d="M176 136h13M178 135v-5M182 135v-8M186 135v-6M178 129l5-4 6-3"/>
    <g stroke="#fff"><circle cx="60" cy="174" r="3.5"/><path d="M58.3 174l1.2 1.2 2.3-2.5"/><circle cx="171" cy="174" r="3.5"/><path d="M169.3 174l1.2 1.2 2.3-2.5"/><circle cx="264" cy="174" r="3.5"/><path d="M262.3 174l1.2 1.2 2.3-2.5"/></g>
  </svg>
  <p class="abs tiny center" style="left:46px;top:92px;width:60px">Falta de Médicos Radiologistas</p>
  <p class="abs tiny center" style="left:122px;top:92px;width:60px">Limitações na qualidade</p>
  <div class="sub-title center" style="left:83px;top:117px;width:62px;font-size:6.2px">A HIPÓTESE</div>
  <p class="abs tiny center" style="left:13px;top:140px;width:70px">Expatriar Profissionais Portugueses</p>
  <p class="abs tiny center" style="left:152px;top:140px;width:60px">Elevado custo</p>
  <p class="abs tiny center" style="left:15px;top:180px;width:90px;color:#fff">Serviço de qualidade Europeia: necessários pelo menos 7 Médicos Radiologistas nas diferentes sub-especialidades</p>
  <p class="abs tiny center" style="left:126px;top:180px;width:90px;color:#fff">Portugal e Brasil também com enorme falta de Médicos</p>
  <p class="abs tiny center" style="left:229px;top:180px;width:70px;color:#fff">Custo elevado fixo</p>
  <footer class="slide-foot"><i class="foot-accent"></i><div class="foot-logo"><i></i><span>VÉRTICE</span></div><span class="foot-url">www.verticetelemed.com | 2</span></footer>
</section>

<section class="slide" style="left:819px;top:340px">
  <header class="slide-head"><h2 class="slide-title">IMAGIOLOGIA EM ANGOLA</h2></header>
  <div class="sub-title" style="left:9px;top:35px">A SOLUÇÃO - TELERADIOLOGIA</div>
  <svg class="abs" style="left:0;top:0" width="320" height="239" role="img" aria-label="Radiologista a trabalhar em estação com vários monitores">
    <defs><linearGradient id="g2" x1="0" x2="1" y1="0" y2="1"><stop offset="0" stop-color="#2a5d92"/><stop offset=".5" stop-color="#4d84b8"/><stop offset="1" stop-color="#c9c3b6"/></linearGradient></defs>
    <polygon points="0,50 320,50 320,203 0,222" fill="url(#g2)"/>
  </svg>
  <footer class="slide-foot"><i class="foot-accent"></i><div class="foot-logo"><i></i><span>VÉRTICE</span></div><span class="foot-url">www.verticetelemed.com | 2</span></footer>
</section>

<section class="slide" style="left:92px;top:623px">
  <header class="slide-head"><h2 class="slide-title">SOBRE NÓS</h2></header>
  <p class="abs" style="left:17px;top:53px;width:70px;font-size:5px;font-weight:700;line-height:1.3">O Centro Internacional de Telemedicina Professor Doutor Rui Tavares nasceu da necessidade de assegurar uma resposta de teleradiologia de elevada qualidade, suportada por um corpo clínico de topo.</p>
  <svg class="abs" style="left:0;top:0" width="320" height="239"><polygon points="91,43 168,43 168,180 126,224 91,224" fill="var(--navy)"/></svg>
  <p class="abs" style="left:95px;top:52px;width:70px;font-size:5px;line-height:1.25;color:#fff">Os nossos médicos são sub-especializados nas diferentes áreas: sistema músculo-esquelético, medicina desportiva, neurorradiologia, abdómen, pélvis, sistema cardiovascular e mama. Todos os nossos exames recebem assim uma consultadoria diferenciada por especialistas de renome, assegurando o máximo rigor diagnóstico.</p>
  <div class="photo" role="img" aria-label="Diagrama de rede de teleradiologia entre centro de serviço, hospitais e radiologistas" style="left:178px;top:46px;width:124px;height:110px;border-radius:50%;background:radial-gradient(circle,#9cc2e3,#d8e3ee 70%,#fff)"></div>
  <svg class="abs" style="left:0;top:0" width="320" height="239" fill="var(--teal)">
    <circle cx="233" cy="165" r="2.5"/><path d="M228 173a5 4 0 0 1 10 0z"/>
    <path d="M176 187a3 3 0 1 1 6 0c0 2-3 5-3 5s-3-3-3-5z" fill="none" stroke="var(--teal)" stroke-width=".8"/>
    <path d="M286 190l4 4 2-2 3 4" fill="none" stroke="var(--teal)" stroke-width=".9"/>
  </svg>
  <p class="abs center" style="left:193px;top:180px;width:80px;font-size:5.5px;font-weight:600">Os melhores Médicos</p>
  <p class="abs center" style="left:146px;top:198px;width:60px;font-size:5.5px;font-weight:600">EM LUANDA</p>
  <p class="abs center" style="left:262px;top:198px;width:56px;font-size:5.5px;font-weight:600">Baixo custo</p>
  <footer class="slide-foot"><i class="foot-accent"></i><div class="foot-logo"><i></i><span>VÉRTICE</span></div><span class="foot-url">www.verticetelemed.com | 2</span></footer>
</section>

<section class="slide" style="left:446px;top:623px">
  <header class="slide-head"><h2 class="slide-title">SOBRE NÓS</h2></header>
  <div class="abs center" style="left:119px;top:39px;width:80px;font-size:9px;font-weight:700">Research</div>
  <svg class="abs" style="left:0;top:0" width="320" height="239">
    <defs><marker id="ah" viewBox="0 0 6 6" refX="5" refY="3" markerWidth="5" markerHeight="5" orient="auto"><path d="M0 0L6 3 0 6z" fill="#4b87b5"/></marker><marker id="ad" viewBox="0 0 6 6" refX="5" refY="3" markerWidth="5" markerHeight="5" orient="auto"><path d="M0 0L6 3 0 6z" fill="#333"/></marker></defs>
    <circle cx="159" cy="67" r="12" fill="#333"/>
    <g stroke="#fff" stroke-width=".9" fill="none"><circle cx="159" cy="65" r="4"/><path d="M157 70h4M157.5 72h3M159 57v-2M152 65h-2M166 65h2M154 60l-1.5-1.5M164 60l1.5-1.5"/></g>
    <circle cx="86" cy="155" r="12" fill="var(--teal)"/><path d="M79 155l4-3 3 2 3-2 5 3-4 3-3-2-3 2z" fill="none" stroke="#fff" stroke-width=".9"/>
    <circle cx="232" cy="155" r="12" fill="var(--blue)"/><path d="M224 153l8-4 8 4-8 4z M228 155v4c2 2 6 2 8 0v-4" fill="#fff"/>
    <g stroke="#4b87b5" stroke-width=".7"><line x1="96" y1="137" x2="131" y2="84" marker-end="url(#ah)"/><line x1="136" y1="86" x2="102" y2="139" marker-end="url(#ah)"/>
      <line x1="186" y1="84" x2="223" y2="139" marker-end="url(#ah)"/><line x1="218" y1="140" x2="182" y2="86" marker-end="url(#ah)"/></g>
    <g stroke="#333" stroke-width=".6"><line x1="113" y1="158" x2="203" y2="158" marker-end="url(#ad)"/><line x1="203" y1="158" x2="113" y2="158" marker-end="url(#ad)"/></g>
  </svg>
  <p class="abs" style="left:60px;top:84px;width:54px;font-size:4.4px;line-height:1.25;color:#4b87b5;text-align:right">Business Opportunities point to new research avenues</p>
  <p class="abs center" style="left:134px;top:90px;width:52px;font-size:4.4px;line-height:1.25">New knowledge improves education</p>
  <p class="abs" style="left:114px;top:121px;width:48px;font-size:4.4px;line-height:1.25;color:#4b87b5">New Knowledge is the source of innovation</p>
  <p class="abs center" style="left:208px;top:113px;width:58px;font-size:4.4px;line-height:1.25;color:#4b87b5">Skills are a key input in research and development</p>
  <p class="abs center" style="left:116px;top:145px;width:90px;font-size:4.4px">Skills are a key input in innovation</p>
  <p class="abs center" style="left:130px;top:166px;width:66px;font-size:4.4px;line-height:1.25">Knowledge of new market developments is important for education</p>
  <div class="abs center" style="left:56px;top:174px;width:60px;font-size:9px;font-weight:600;color:var(--teal)">Business</div>
  <div class="abs center" style="left:200px;top:174px;width:64px;font-size:9px;font-weight:600;color:var(--blue)">Education</div>
  <footer class="slide-foot"><i class="foot-accent"></i><div class="foot-logo"><i></i><span>VÉRTICE</span></div><span class="foot-url">www.verticetelemed.com | 2</span></footer>
</section>

<section class="slide" style="left:819px;top:623px">
  <header class="slide-head"><h2 class="slide-title">RUI TAVARES</h2></header>
  <div class="photo" role="img" aria-label="Retrato do diretor clínico" style="left:11px;top:47px;width:86px;height:86px;border-radius:50%;border:1.5px solid var(--teal);background:radial-gradient(circle,#6f6f72,#2c2c30)"></div>
  <div class="abs" style="left:105px;top:46px;width:96px;font-size:4.3px;line-height:1.25">
    <p style="font-size:5.6px;font-weight:700;color:var(--teal)">Educação Universitária</p>
    <p style="font-weight:600;color:var(--teal)">Licenciado em Medicina pela Faculdade de Medicina da Universidade do Atlântico (FMA), com a classificação final de 17,17 valores (2000).</p>
    <p style="margin-top:4px">Doutorado em Medicina pela FMA, aprovado por Unanimidade com Distinção e Louvor (2012).</p>
    <p style="margin-top:4px;font-size:5.6px;font-weight:700;color:var(--teal)">Educação Pós-Graduada</p>
    <p>Médico Interno de Imagiologia e Radiodiagnóstico do Hospital Universitário da Estrela (2003 a 2008).</p>
    <p style="margin-top:4px">Visiting Clinical Fellow – Vascular Imaging, Pacific Coast University (2008).</p>
    <p style="margin-top:4px">Visiting Clinical Fellow – Musculoskeletal Imaging, Service de Radiologie Ostéoarticulaire, Hôpital Lumière, Lyon (2008).</p>
  </div>
  <svg class="abs" style="left:0;top:0" width="320" height="239"><polygon points="203,41 320,41 320,225 272,225 203,190" fill="var(--navy)"/></svg>
  <div class="abs" style="left:213px;top:46px;width:100px;font-size:4.3px;line-height:1.25;color:#fff">
    <p style="font-size:5.6px;font-weight:700">Funções Actuais</p>
    <p>CEO, Centro Vértice de Telemedicina (desde 2013).</p>
    <p style="margin-top:4px">Membro da Comissão Editorial do “Global Review of Orthopaedics” (desde 2014).</p>
    <p style="margin-top:4px">Grau de Consultor (Imagiologia) pelo Colégio Nacional de Medicina (desde 2018).</p>
    <p style="margin-top:4px">Professor Auxiliar Convidado e Regente de Disciplina da Tejo Medical School (desde 2018).</p>
    <p style="margin-top:4px">Investigador do Integrated Health Research Center, IHRC/TMS (desde 2018).</p>
  </div>
  <footer class="slide-foot"><i class="foot-accent"></i><div class="foot-logo"><i></i><span>VÉRTICE</span></div><span class="foot-url">www.verticetelem</span></footer>
</section>

<section class="slide" style="left:92px;top:887px">
  <header class="slide-head"><h2 class="slide-title">SOBRE NÓS</h2></header>
  <div class="sub-title center" style="left:112px;top:43px;width:100px">CUSTOS CONTROLADOS</div>
  <svg class="abs" style="left:0;top:0" width="320" height="239" role="img" aria-label="Imagens médicas em tons azuis sob faixa de cor">
    <defs><linearGradient id="g3" x1="0" x2="1"><stop offset="0" stop-color="#3b8ab4"/><stop offset="1" stop-color="#4795bd"/></linearGradient></defs>
    <polygon points="0,132 74,66 320,66 320,188 0,188" fill="url(#g3)"/>
  </svg>
  <svg class="abs" style="left:0;top:0" width="320" height="239" fill="none" stroke="#fff" stroke-width=".8">
    <g transform="rotate(-38 34 71)" stroke="var(--navy)"><rect x="14" y="60" width="42" height="22"/><line x1="22" y1="60" x2="22" y2="82" stroke-dasharray="2 1.5"/><text x="35" y="76" fill="var(--navy)" stroke="none" font-size="13" font-family="Poppins,sans-serif">$</text></g>
    <circle cx="107" cy="96" r="9"/><rect x="102" y="92" width="10" height="7"/>
    <circle cx="216" cy="100" r="9"/><path d="M212 100l3 3 6-7"/>
    <circle cx="56" cy="141" r="9"/><text x="52.5" y="145" fill="#fff" stroke="none" font-size="10" font-family="Poppins,sans-serif">$</text>
    <circle cx="163" cy="141" r="9"/><rect x="159" y="136" width="8" height="10"/>
    <circle cx="268" cy="141" r="9"/><path d="M264 137h8v9h-8zM266 140h4M266 142h4"/>
  </svg>
  <p class="abs tiny center" style="left:72px;top:112px;width:70px;color:#fff">Despesa com a montagem da plataforma informática fica completamente do nosso lado</p>
  <p class="abs tiny center" style="left:181px;top:116px;width:70px;color:#fff">Não existe qualquer pagamento inicial</p>
  <p class="abs tiny center" style="left:21px;top:155px;width:70px;color:#fff">Não existem quaisquer custos fixos ou um mínimo de exames obrigatório</p>
  <p class="abs tiny center" style="left:126px;top:155px;width:74px;color:#fff">Temos simplesmente um preço por relatório</p>
  <p class="abs tiny center" style="left:233px;top:155px;width:70px;color:#fff">São faturados apenas os relatórios efectivados</p>
  <footer class="slide-foot"><i class="foot-accent"></i><div class="foot-logo"><i></i><span>VÉRTICE</span></div><span class="foot-url">www.verticetelemed.com | 2</span></footer>
</section>

</body>
</html>
```